Consulting company with focus on aviation needs

We need a new business card design for our company. The company consults with multiple players in the industry like manufacturers and airlines. It is also a supplier and an inter-company level. Given the targeted industry (aviation) it should be both kind of serious, sound, secure, classy, ​​but also a bit technical, innovative. Should not be too playful, however, "fresh", "airy", "ligth" and "suprising" are suitabe attributes. The existing logo shall be used.

Airlines

```html
<!DOCTYPE html>
<html lang="en">
<head>
<meta charset="utf-8">
<title>Aerovant Business Card</title>
<link href="https://fonts.googleapis.com/css2?family=Montserrat:wght@500;600&family=Quicksand:wght@400;500&display=swap" rel="stylesheet">
<style>
  :root {
    --page: #e9eaea;
    --card: #ffffff;
    --ink: #5a5e60;
    --ink-soft: #8a8e90;
    --teal: #17987d;
    --teal-deep: #138a71;
    --on-teal: #e8f6f2;
    --accent: #f39a2b;
  }
  * { margin: 0; padding: 0; box-sizing: border-box; }
  html, body { width: 1200px; height: 797px; overflow: hidden; }
  body {
    background: var(--page);
    font-family: "Quicksand", sans-serif;
    color: var(--ink);
    position: relative;
  }
  .card {
    position: absolute;
    top: 250px;
    width: 525px;
    height: 300px;
    background: var(--card);
    box-shadow: 0 8px 24px rgba(0,0,0,0.12);
    overflow: hidden;
  }
  .card--front { left: 45px; }
  .card--back { left: 630px; }

  .brand {
    display: flex;
    align-items: center;
    gap: 12px;
    font-family: "Montserrat", sans-serif;
    font-weight: 500;
    color: var(--ink);
    letter-spacing: 0.14em;
  }
  .brand__dot {
    border-radius: 50%;
    background: var(--teal);
    flex: none;
  }
  .card--front .brand {
    position: absolute;
    left: 50%; top: 50%;
    transform: translate(-50%, -50%);
    font-size: 34px;
  }
  .card--front .brand__dot { width: 30px; height: 30px; }

  .card--back .brand {
    position: absolute;
    top: 30px; right: 30px;
    font-size: 17px;
    gap: 7px;
  }
  .card--back .brand__dot { width: 16px; height: 16px; }

  .holder {
    position: absolute;
    left: 32px; top: 76px;
  }
  .holder__name {
    font-family: "Montserrat", sans-serif;
    font-weight: 600;
    font-size: 21px;
    letter-spacing: 0.02em;
    color: var(--ink);
    text-transform: uppercase;
  }
  .holder__role {
    font-size: 12px;
    color: var(--ink-soft);
    margin-top: 1px;
  }

  .contact-band {
    position: absolute;
    left: 0; right: 0; bottom: 0;
    height: 160px;
    background: linear-gradient(135deg, var(--teal) 0%, var(--teal-deep) 100%);
    display: grid;
    grid-template-columns: 1fr 1fr;
    align-content: center;
    row-gap: 24px;
    padding: 0 32px;
  }
  .contact {
    display: flex;
    align-items: center;
    gap: 16px;
    font-size: 12.5px;
    color: var(--on-teal);
    letter-spacing: 0.02em;
  }
  .contact svg {
    width: 16px; height: 16px;
    fill: none;
    stroke: var(--on-teal);
    stroke-width: 1.3;
    stroke-linecap: round;
    stroke-linejoin: round;
    flex: none;
  }
</style>
</head>
<body>

  <section class="card card--front" aria-label="Card front">
    <div class="brand"><span class="brand__dot"></span>AEROVANT</div>
  </section>

  <section class="card card--back" aria-label="Card back">
    <div class="brand"><span class="brand__dot"></span>AEROVANT</div>

    <div class="holder">
      <p class="holder__name">Elias Marlow</p>
      <p class="holder__role">Manager</p>
    </div>

    <div class="contact-band">
      <div class="contact">
        <svg viewBox="0 0 16 16" aria-hidden="true"><rect x="4.5" y="1.5" width="7" height="13" rx="1.2"/><line x1="7" y1="12.3" x2="9" y2="12.3"/></svg>
        <span>123 456 7890</span>
      </div>
      <div class="contact">
        <svg viewBox="0 0 16 16" aria-hidden="true"><rect x="1.5" y="2.5" width="13" height="8.5" rx="0.8"/><line x1="8" y1="11" x2="8" y2="13.5"/><line x1="5" y1="13.5" x2="11" y2="13.5"/></svg>
        <span>www.eliasmarlow.com</span>
      </div>
      <div class="contact">
        <svg viewBox="0 0 16 16" aria-hidden="true"><rect x="1.5" y="3.5" width="13" height="9" rx="0.8"/><polyline points="1.8,4 8,9 14.2,4"/></svg>
        <span>info@eliasmarlow.com</span>
      </div>
      <div class="contact">
        <svg viewBox="0 0 16 16" aria-hidden="true"><path d="M8 14.5s-4.5-4.6-4.5-8a4.5 4.5 0 0 1 9 0c0 3.4-4.5 8-4.5 8z"/><circle cx="8" cy="6.5" r="1.6"/></svg>
        <span>Address Line</span>
      </div>
    </div>
  </section>

</body>
</html>
```